OLVAK Web Design (Need help to re-design our website)

We need someone to help us re-design our website and launch it. All contents for the website are ready. (https://olvak.example.au/)

-Rearrange categories:
1. Heating & Cooling
2. Remove Home Appliance
3. Remove Entertainment

Home page - redesign (It will be a nice touch if the banner is in the loop).

NOTE:
-Brand colour blue and orange.
-Try using professional fonts (Example: Helvetica, etc.)
-The website's Footer should be readable and use light colour.

Target Market(s)

Residentials & commercial buildings

Industry/Entity Type

Heat Ventilation and Cooling Industry, Technology , Renewables

Coding

Coded - Design and coding required

Colors
0094D4
00A9DD
6FCCEA
C7EBF8
E9F6FB
59FF00
82FF00
B8FF75
E3FFCB
F4FFEA
F0912C
F2A743
F7CA91
FBE8D2
FDF5EE

Requirements
Nice to have
• Effects/transition on the words/copy/images.

```html
<!DOCTYPE html>
<html lang="en">
<head>
<meta charset="utf-8">
<title>OLVAK – Heating &amp; Cooling</title>
<link href="https://fonts.googleapis.com/css2?family=Poppins:wght@400;500;600;700&display=swap" rel="stylesheet">
<style>
:root{
  --blue:#1664b0;
  --blue-dark:#11569a;
  --orange:#f68f22;
  --white:#ffffff;
  --ink:#1d1d1d;
  --muted:#6b6b6b;
  --panel:#f4f4f4;
  --line:#e2e2e2;
}
*{box-sizing:border-box;margin:0;padding:0}
html,body{width:1200px;height:3871px;overflow:hidden}
body{position:relative;font-family:"Poppins",Helvetica,Arial,sans-serif;color:var(--ink);background:var(--white)}
.abs{position:absolute}
.brand{font-weight:600;letter-spacing:5px;color:var(--blue);display:flex;align-items:center;gap:14px}
.brand-dot{width:30px;height:30px;border-radius:50%;background:var(--orange)}
.leaf-btn{position:absolute;display:flex;align-items:center;justify-content:center;background:var(--orange);color:var(--white);border-radius:48px 0 48px 0;font-weight:500;letter-spacing:.5px}

/* header */
.site-header{top:0;left:0;width:1200px;height:135px}
.site-header .brand{left:76px;top:42px;font-size:46px}
.social-mini{top:40px;display:flex;gap:4px;left:614px}
.social-mini span{width:18px;height:18px;border-radius:3px;background:var(--blue)}
.search{left:672px;top:30px;width:215px;height:36px;border:1.5px solid #bbb;border-radius:18px;font-size:12px;color:#999;padding:9px 16px}
.search svg{position:absolute;right:14px;top:10px}
.book{left:902px;top:30px;width:224px;height:36px;background:var(--blue);color:var(--white);font-size:14px;border-radius:30px 0 30px 0;display:flex;align-items:center;justify-content:center}
.main-nav{top:86px;left:606px;display:flex;gap:31px;font-size:13px;color:var(--ink)}
.main-nav .active{color:var(--orange);border-bottom:2px solid var(--orange);padding-bottom:6px}

/* hero */
.hero{top:135px;left:0;width:1200px;height:630px;background:var(--blue);overflow:hidden}
.hero-kicker{left:75px;top:90px;color:var(--orange);font-size:40px;font-weight:600}
.hero-title{left:75px;top:140px;color:var(--white);font-size:79px;font-weight:700;line-height:76px}
.hero-sub{left:76px;top:318px;color:var(--white);font-size:39px;font-weight:500}
.hero .leaf-btn{left:78px;top:420px;width:257px;height:63px;font-size:21px}
.dots{left:392px;top:544px;display:flex;gap:4px}
.dots span{width:12px;height:12px;border-radius:50%;background:#8aa8cf}
.dots span:first-child{background:var(--white)}
.hero-brand{left:720px;top:128px;font-size:52px}
.hero-unit{left:593px;top:225px;width:540px;height:260px;border-radius:14px;background:linear-gradient(#fbfbfb,#e6e6e6)}

/* products */
.section-title{left:0;width:1200px;display:flex;justify-content:center;align-items:center;gap:22px;color:var(--blue);font-weight:600;font-size:54px}
.section-title i{width:44px;height:44px;background:var(--orange);display:block}
.card{width:503px;height:270px;background:var(--white);box-shadow:0 2px 10px rgba(0,0,0,.14)}
.card .shot{position:absolute;left:100px;right:100px;top:20px;height:210px;background:linear-gradient(#f5f5f5,#dcdcdc);border-radius:8px}
.card-label{width:422px;height:62px;background:var(--blue);color:var(--white);font-size:21px;font-weight:600;display:flex;align-items:center;justify-content:space-between;padding:0 26px 0 40px}

/* about */
.about{top:1802px;left:0;width:1200px;height:630px;background:var(--blue);overflow:hidden}
.about-orange{left:0;top:0;width:560px;height:630px;background:var(--orange);clip-path:polygon(0 0,450px 0,560px 50%,450px 630px,0 630px)}
.about-ring{left:46px;top:-8px;width:646px;height:646px;border-radius:50%;background:var(--white)}
.about-photo{left:78px;top:24px;width:582px;height:582px;border-radius:50%;background:linear-gradient(135deg,#cfd6de,#5a7fb5 60%,#2d4f86)}
.about-mark{left:900px;top:102px;width:44px;height:44px;background:var(--orange)}
.about h2{position:absolute;left:722px;width:400px;top:170px;text-align:center;color:var(--white);font-size:50px;font-weight:600}
.about p{position:absolute;left:737px;top:256px;width:370px;font-size:14px;line-height:27px;color:var(--white);text-align:justify;text-align-last:center}
.about .leaf-btn{left:795px;top:460px;width:255px;height:64px;font-size:21px}

/* contact */
.contact-sub{left:0;width:1200px;top:2671px;text-align:center;font-size:24px;color:#333}
.contact-panel{left:75px;top:2748px;width:1050px;height:814px;background:var(--panel)}
.info{left:122px;display:flex;align-items:center;gap:18px}
.info .ico{width:74px;height:74px;border-radius:50%;display:flex;align-items:center;justify-content:center}
.info h4{font-size:21px;font-weight:600;letter-spacing:.5px}
.info p{font-size:17px;line-height:25px}
.form{left:470px;top:2818px;width:609px;height:672px;background:var(--white)}
.form label{position:absolute;left:72px;font-size:13px;font-weight:500}
.field{position:absolute;border:1.5px solid var(--line);font-size:13px;color:#999;padding:14px 20px}
.form .leaf-btn{left:195px;top:554px;width:220px;height:63px;font-size:21px}

/* footer */
.site-footer{top:3620px;left:0;width:1200px;height:200px;background:var(--blue)}
.site-footer .brand{left:78px;top:82px;font-size:40px;color:var(--white)}
.foot-nav{left:332px;top:104px;display:flex;gap:32px;color:var(--white);font-size:13px}
.news-label{left:833px;top:60px;color:var(--white);font-size:17px}
.news{left:822px;top:93px;width:305px;height:43px;border:2px solid var(--orange);background:var(--orange);border-radius:4px;display:flex;align-items:center;justify-content:space-between;padding:0 6px 0 16px;color:var(--white);font-size:12px}
.news b{background:var(--blue);font-weight:400;font-size:14px;padding:6px 16px;border-radius:4px}
.copy-bar{top:3820px;left:0;width:1200px;height:51px;background:var(--orange)}
.copy-bar p{position:absolute;left:78px;top:17px;color:var(--white);font-size:13px}
.copy-bar .social{position:absolute;right:72px;top:9px;display:flex;gap:6px}
.copy-bar .social span{width:30px;height:30px;border-radius:50%;background:var(--blue)}
</style>
</head>
<body>

<header class="abs site-header">
  <div class="abs brand"><span class="brand-dot"></span>OLVAK</div>
  <div class="abs social-mini"><span></span><span></span></div>
  <div class="abs search">Search...
    <svg width="16" height="16" viewBox="0 0 16 16"><circle cx="7" cy="7" r="5" fill="none" stroke="#999" stroke-width="1.5"/><line x1="11" y1="11" x2="15" y2="15" stroke="#999" stroke-width="1.5"/></svg>
  </div>
  <div class="abs book">Book Anppointment</div>
  <nav class="abs main-nav">
    <span class="active">HOME</span><span>OUR STORY</span><span>HEATING &amp; COOLING ▾</span><span>SUPPORT</span><span>CONTACT US</span>
  </nav>
</header>

<section class="abs hero">
  <svg class="abs" style="left:0;top:0" width="1200" height="630">
    <rect x="930" y="0" width="270" height="630" fill="var(--orange)"/>
    <circle cx="856" cy="315" r="324" fill="var(--white)"/>
  </svg>
  <div class="abs hero-kicker">Revolutionise</div>
  <h1 class="abs hero-title">HEATING &amp;<br>COOLING</h1>
  <div class="abs hero-sub">Industry Australiawide</div>
  <div class="leaf-btn">EXPLORE</div>
  <div class="abs dots"><span></span><span></span><span></span></div>
  <div class="abs brand hero-brand"><span class="brand-dot"></span>OLVAK</div>
  <div class="abs hero-unit" role="img" aria-label="Wall-mounted split system air conditioner"></div>
</section>

<h2 class="abs section-title" style="top:872px"><i></i>HEATING &amp; COOLING</h2>

<div class="abs card" style="left:75px;top:1010px"><div class="shot" role="img" aria-label="Heat pump water heater units"></div></div>
<div class="abs card-label" style="left:116px;top:1248px">Heat Pump <span>→</span></div>
<div class="abs card" style="left:618px;top:1010px"><div class="shot" role="img" aria-label="Split system air conditioner"></div></div>
<div class="abs card-label" style="left:659px;top:1248px">Air Conditioners <span>→</span></div>
<div class="abs card" style="left:75px;top:1363px"><div class="shot" role="img" aria-label="Swimming pool heat pump unit"></div></div>
<div class="abs card-label" style="left:116px;top:1600px">Swimming Pool Heat Pump <span>→</span></div>
<div class="abs card" style="left:618px;top:1363px"><div class="shot" role="img" aria-label="Monoblock heat pump outdoor unit"></div></div>
<div class="abs card-label" style="left:659px;top:1600px">Monoblock Heat Pump <span>→</span></div>

<section class="abs about">
  <div class="abs about-orange"></div>
  <div class="abs about-ring"></div>
  <div class="abs about-photo" role="img" aria-label="Technician fitting pipework with a wrench"></div>
  <div class="abs about-mark"></div>
  <h2>ABOUT OLVAK</h2>
  <p>OLVAK is a company dedicated to manufacturing and installing energy-efficient products that reduce energy consumption, save costs, and promote sustainability. Our mission is to help individuals and businesses reduce their carbon footprint while also enhancing their comfort and quality of life.</p>
  <div class="leaf-btn">READ MORE</div>
</section>

<h2 class="abs section-title" style="top:2555px"><i></i>CONTACT US</h2>
<p class="abs contact-sub">Enter your details below to get started.</p>

<div class="abs contact-panel"></div>
<div class="abs info" style="top:2946px">
  <div class="ico" style="background:var(--blue)"><svg width="30" height="38" viewBox="0 0 30 38"><path d="M15 2a12 12 0 0 0-12 12c0 9 12 22 12 22s12-13 12-22A12 12 0 0 0 15 2z" fill="#fff"/><circle cx="15" cy="14" r="5" fill="var(--blue)"/></svg></div>
  <div><h4>LOCATION</h4><p>48 Harbourline Rd, Westvale<br>VIC 3999</p></div>
</div>
<div class="abs info" style="top:3128px">
  <div class="ico" style="background:var(--orange)"><svg width="34" height="34" viewBox="0 0 24 24"><path d="M6.6 10.8a15 15 0 0 0 6.6 6.6l2.2-2.2a1 1 0 0 1 1-.25 11.4 11.4 0 0 0 3.6.6 1 1 0 0 1 1 1V20a1 1 0 0 1-1 1A17 17 0 0 1 3 4a1 1 0 0 1 1-1h3.5a1 1 0 0 1 1 1 11.4 11.4 0 0 0 .6 3.6 1 1 0 0 1-.25 1z" fill="#fff"/></svg></div>
  <div><h4>CALL US</h4><p>1800 555 019</p></div>
</div>
<div class="abs info" style="top:3320px">
  <div class="ico" style="background:var(--blue)"><svg width="38" height="28" viewBox="0 0 38 28"><rect x="1" y="1" width="36" height="26" fill="none" stroke="#fff" stroke-width="2.5"/><path d="M1 1l18 14L37 1" fill="none" stroke="#fff" stroke-width="2.5"/></svg></div>
  <div><h4>EMAIL US</h4><p>info@olvak.example.au</p></div>
</div>

<form class="abs form">
  <label style="top:42px">TELL US YOUR NAME *</label>
  <div class="field" style="left:72px;top:67px;width:223px;height:46px">First Name:</div>
  <div class="field" style="left:315px;top:67px;width:223px;height:46px">Last Name:</div>
  <label style="top:146px">ENTER YOUR EMAIL *</label>
  <div class="field" style="left:72px;top:172px;width:466px;height:46px">Email:</div>
  <label style="top:249px">ENTER PHONE NUMBER</label>
  <div class="field" style="left:72px;top:275px;width:466px;height:46px">Phone:</div>
  <label style="top:353px">MESSAGE *</label>
  <div class="field" style="left:72px;top:380px;width:466px;height:150px">Write us a message</div>
  <div class="leaf-btn">SUBMIT</div>
</form>

<footer class="abs site-footer">
  <div class="abs brand"><span class="brand-dot"></span>OLVAK</div>
  <nav class="abs foot-nav"><span>OUR STORY</span><span>HEATING &amp; COOLING</span><span>SUPPORT</span><span>CONTACT US</span></nav>
  <div class="abs news-label">Join Our Newsletter</div>
  <div class="abs news">Enter Your Email Address <b>Sign Up</b></div>
</footer>
<div class="abs copy-bar">
  <p>© Copyright 2024 OLVAK - All rights reserved.</p>
  <div class="social"><span></span><span></span><span></span></div>
</div>

</body>
</html>
```